Bluefern Slimming Clinic

build a landing page website using the content from this websites. we want to copy all the content from harrowvalecourses.com but make page look more professional. we dont have a logo yet but url is www.bluefernslimmingclinic.com
https://quillbanktrimalliance.com/home-page
https://www.harrowvalecourses.com/

Target Market(s)

people looking to open a weightloss clinic or a franchise opportunity

Coding

Coded - Design and coding required

Number of Pages Required

3 page

Requirements
Must have
• copy all content from other site https://www.harrowvalecourses.com/

```html
<!DOCTYPE html>
<html lang="en">
<head>
<meta charset="utf-8">
<title>Bluefern Slimming Clinic – Start Your Own Weight Loss Clinic</title>
<link href="https://fonts.googleapis.com/css2?family=Figtree:wght@400;500;600;700;800&family=Arimo:wght@400;700&display=swap" rel="stylesheet">
<style>
:root{
  --blue:#1b4d8f;
  --blue-deep:#144a8c;
  --red:#d3202b;
  --navy:#0b1a33;
  --cream:#f6efe7;
  --ink:#2b2b2b;
  --light:#f2f4f8;
}
*{box-sizing:border-box;margin:0;padding:0}
html,body{width:1200px;height:4079px;overflow:hidden}
body{font-family:"Arimo",Arial,sans-serif;color:var(--ink);background:#fff;position:relative}
.abs{position:absolute}
.btn{position:absolute;display:flex;align-items:center;justify-content:center;border-radius:30px;font-family:"Figtree",Arial,sans-serif;font-weight:700;font-size:11.5px;letter-spacing:.3px;text-transform:uppercase}
.btn-red{background:var(--red);color:#fff}
.btn-ghost{border:1.5px solid var(--blue);color:var(--blue);background:#fff}

/* header */
.site-header{left:0;top:0;width:1200px;height:114px;background:var(--cream);border-bottom:1px solid #e6ddd2}
.brand-name{font-family:"Figtree",Arial,sans-serif;font-weight:700;font-size:21px;line-height:25px;color:var(--blue)}
.topline{font-size:11.5px;color:var(--blue);display:flex;align-items:center;gap:7px}
.nav{top:66px;left:432px;font-family:"Figtree",Arial,sans-serif;font-weight:700;font-size:12px;color:#222}
.nav span{position:absolute;white-space:nowrap}

/* hero */
.hero{left:0;top:114px;width:1200px;height:666px;background:var(--cream)}
.hero-photo{left:475px;top:40px;width:725px;height:626px;background:linear-gradient(120deg,#efe7dc 0%,#e3dcd3 40%,#cfd6de 70%,#b9c4cf 100%)}
.eyebrow{font-family:"Figtree",Arial,sans-serif;font-weight:700;font-size:11px;color:#222;letter-spacing:.3px}
.hero h1{font-family:"Figtree",Arial,sans-serif;font-weight:700;font-size:50px;line-height:61px;color:var(--blue)}
.copy p{font-size:13.5px;line-height:20.5px;color:#333;margin-bottom:20px}

/* offer */
.offer-card{left:85px;top:758px;width:1030px;height:352px;background:#fff;box-shadow:0 6px 30px rgba(20,40,80,.10)}
.section-title{font-family:"Figtree",Arial,sans-serif;font-weight:700;color:var(--blue);text-align:center}
.section-title em{font-style:normal;color:var(--red)}
.offer-item{position:absolute;width:250px;text-align:center;top:140px}
.offer-item svg{display:block;margin:0 auto 30px}
.offer-item p{font-family:"Figtree",Arial,sans-serif;font-weight:600;font-size:18.5px;line-height:25px;color:#3a3a3a}

/* wellness */
.doctor-photo{left:142px;top:1180px;width:357px;height:557px;background:linear-gradient(180deg,#f4f5f7 0%,#e6e9ed 60%,#dcdfe5 100%)}
.kicker{font-family:"Figtree",Arial,sans-serif;font-weight:700;font-size:18.5px;color:var(--red)}
.big-title{font-family:"Figtree",Arial,sans-serif;font-weight:700;font-size:36px;color:var(--blue)}

/* compare */
.compare{left:0;top:1737px;width:1200px;height:426px;background:linear-gradient(90deg,#34455a 0%,#3d4e63 50%,#4a596c 100%)}
.compare h2{font-family:"Figtree",Arial,sans-serif;font-weight:700;font-size:39px;color:#fff;text-align:center;position:absolute;left:0;width:1200px;top:56px}
.check{position:absolute;display:flex;align-items:center;gap:14px;font-family:"Figtree",Arial,sans-serif;font-weight:700;font-size:19.5px;color:#fff}
.check i{width:21px;height:21px;border-radius:50%;background:var(--red);display:flex;align-items:center;justify-content:center}

/* steps */
.steps{left:0;top:2163px;width:1200px;height:639px;background:#fff}
.world{left:300px;top:160px;width:600px;height:440px;background:radial-gradient(ellipse at center,#f1f3f6 0%,#f7f8fa 55%,#fff 75%)}
.step{position:absolute;width:260px;text-align:center}
.step h3{font-family:"Figtree",Arial,sans-serif;font-weight:700;font-size:25px;color:var(--blue);margin-bottom:12px}
.step p{font-family:"Figtree",Arial,sans-serif;font-weight:600;font-size:13.5px;line-height:19px;color:#555}

/* badges */
.badges{left:0;top:2802px;width:1200px;height:166px;background:var(--light)}
.badge{position:absolute}

/* contact */
.contact-photo{left:0;top:2968px;width:601px;height:608px;background:linear-gradient(110deg,#eef0f1 0%,#e3dfd9 45%,#c9c3bb 100%)}
.contact{left:601px;top:2968px;width:599px;height:608px;background:var(--blue-deep)}
.field{position:absolute;background:#fff;border-radius:2px;font-family:"Figtree",Arial,sans-serif;font-weight:600;font-size:11.5px;color:#333;padding:15px 20px}

/* footer */
.footer{left:0;top:3576px;width:1200px;height:503px;background:var(--navy);color:#fff}
.footer .brand-name{color:#fff}
.f-head{font-family:"Figtree",Arial,sans-serif;font-weight:700;font-size:17px;color:#fff;letter-spacing:.3px}
.f-link{position:absolute;font-family:"Figtree",Arial,sans-serif;font-weight:600;font-size:11.5px;color:#fff}
.f-info{position:absolute;display:flex;gap:12px;font-size:13px;line-height:22px}
.f-rule{left:0;top:412px;width:1200px;height:1px;background:#25334d}
</style>
</head>
<body>

<header class="abs site-header">
  <div class="abs brand-name" style="left:85px;top:34px">Bluefern<br>Slimming Clinic</div>
  <div class="abs topline" style="left:728px;top:14px">
    <svg width="15" height="11" viewBox="0 0 15 11"><rect x=".5" y=".5" width="14" height="10" fill="var(--blue)"/><path d="M1 1l6.5 5L14 1" stroke="#fff" fill="none"/></svg>
    hello@harrowvalecourses.com
  </div>
  <div class="abs topline" style="left:1011px;top:14px">
    <svg width="13" height="13" viewBox="0 0 24 24"><path d="M6.6 10.8a15 15 0 006.6 6.6l2.2-2.2c.3-.3.7-.4 1-.2 1.1.4 2.3.6 3.6.6.6 0 1 .4 1 1V20c0 .6-.4 1-1 1A17 17 0 013 4c0-.6.4-1 1-1h3.5c.6 0 1 .4 1 1 0 1.3.2 2.5.6 3.6.1.3 0 .7-.2 1z" fill="var(--blue)"/></svg>
    877-555-0142
  </div>
  <nav class="abs nav">
    <span style="left:0">HOME</span>
    <span style="left:78px">ABOUT US</span>
    <span style="left:173px">WHAT WE OFFER</span>
    <span style="left:306px">COMPARE</span>
    <span style="left:405px">FAQ</span>
    <span style="left:454px">CONTACT</span>
  </nav>
  <div class="btn btn-red" style="left:975px;top:52px;width:139px;height:41px">Request Now</div>
</header>

<section class="abs hero">
  <div class="abs hero-photo" role="img" aria-label="Photo of a doctor in a white coat working at a laptop in a bright clinic office"></div>
  <div class="abs eyebrow" style="left:87px;top:97px">WELCOME THERE!</div>
  <h1 class="abs" style="left:82px;top:118px;width:560px">Start Your Own Profitable Weight Loss Clinic!</h1>
  <div class="abs copy" style="left:87px;top:311px;width:520px">
    <p>We are not a weight loss franchise – you are simply buying our business model, training and support for one low fee. Please read about us, look at what we offer and compare us to weight loss franchises in the marketplace.</p>
    <p>We offer you a free market analysis and sample break even analysis for your area.</p>
    <p>We think you will be happy you found us!</p>
  </div>
  <div class="btn btn-red" style="left:87px;top:489px;width:139px;height:41px">Learn More</div>
</section>

<section class="abs offer-card">
  <h2 class="section-title" style="position:absolute;left:0;width:1030px;top:48px;font-size:30px">WHAT WE <em>OFFER</em></h2>
  <div class="offer-item" style="left:27px">
    <svg width="66" height="68" viewBox="0 0 66 68" fill="none" stroke="var(--blue)" stroke-width="2"><rect x="26" y="4" width="36" height="26"/><path d="M32 12h24M32 18h18M32 24h20"/><circle cx="14" cy="22" r="5"/><path d="M6 40v-6a8 8 0 0116 0v6l10-8"/><circle cx="10" cy="52" r="4"/><circle cx="26" cy="52" r="4"/><circle cx="42" cy="52" r="4"/><circle cx="58" cy="52" r="4"/><path d="M3 66v-4a7 7 0 0114 0v4M19 66v-4a7 7 0 0114 0v4M35 66v-4a7 7 0 0114 0v4M51 66v-4a7 7 0 0114 0v4M2 44h62"/></svg>
    <p>One-on-one Business &amp;<br>Medical Training</p>
  </div>
  <div class="offer-item" style="left:284px">
    <svg width="74" height="68" viewBox="0 0 74 68" fill="none" stroke="var(--blue)" stroke-width="2"><path d="M20 26l24-16v36L20 36z"/><rect x="12" y="26" width="8" height="10"/><path d="M44 18a10 10 0 010 20M50 8l6-5M54 20h8M50 32l6 5"/><path d="M2 52h14l12 4h10a3 3 0 010 6H24M16 48v16M38 58l18-8a3 3 0 013 5L40 66H20"/></svg>
    <p>Marketing &amp;<br>Advertising Training</p>
  </div>
  <div class="offer-item" style="left:524px">
    <svg width="70" height="70" viewBox="0 0 70 70" fill="none" stroke="var(--blue)" stroke-width="2"><rect x="4" y="6" width="40" height="58"/><rect x="16" y="2" width="16" height="8"/><path d="M10 20l3 3 5-5M22 21h16M10 32l3 3 5-5M22 33h16M10 44l3 3 5-5M22 45h16M22 55h12"/><path d="M52 26c-6 0-8 6-6 12 2 8 4 12 6 14 2-2 4-6 6-14 2-6 0-12-6-12zM52 26v-6l4-4"/><path d="M44 64h20"/></svg>
    <p>Diets, Patient<br>Protocols &amp; Programs</p>
  </div>
  <div class="offer-item" style="left:776px">
    <svg width="60" height="66" viewBox="0 0 60 66" fill="none" stroke="var(--blue)" stroke-width="2"><rect x="4" y="4" width="26" height="58"/><rect x="30" y="22" width="26" height="40"/><path d="M11 14h12M11 24h12M11 34h12M11 44h12M37 32h12M37 42h12M37 52h12M2 62h56"/></svg>
    <p>Office &amp; Operations<br>Manuals</p>
  </div>
</section>

<section>
  <div class="abs doctor-photo" role="img" aria-label="Photo of a smiling male doctor in a white coat with a stethoscope, arms crossed"></div>
  <div class="abs kicker" style="left:557px;top:1207px">Start Your Own</div>
  <h2 class="abs big-title" style="left:557px;top:1232px">Weight Loss &amp; Wellness Center</h2>
  <div class="abs copy" style="left:557px;top:1298px;width:520px">
    <p>Bluefern Slimming now offers our model to you so you can add weight loss and wellness programs to your existing medical practice or open a stand alone weight loss and wellness center.</p>
    <p>We are not a weight loss franchise – you are simply buying our business model, training and support for one low fee. Please read about us, look at what we offer and compare us to weight loss franchises in the marketplace.</p>
    <p>We now offer you a free market analysis and sample break even analysis for your area. Please see our contact page.</p>
    <p>We think you will be happy you found us!</p>
  </div>
  <div class="btn btn-red" style="left:557px;top:1592px;width:154px;height:39px">More Details</div>
  <div class="btn btn-ghost" style="left:736px;top:1589px;width:154px;height:39px">Ask an Expert</div>
</section>

<section class="abs compare" role="img" aria-label="Dark blue-tinted photo of a doctor consulting with a patient">
  <h2>Compare</h2>
  <div class="check" style="left:241px;top:140px"><i><svg width="11" height="9" viewBox="0 0 11 9"><path d="M1 4.5l3 3L10 1" stroke="#fff" stroke-width="2" fill="none"/></svg></i>No Franchise Fees</div>
  <div class="check" style="left:241px;top:191px"><i><svg width="11" height="9" viewBox="0 0 11 9"><path d="M1 4.5l3 3L10 1" stroke="#fff" stroke-width="2" fill="none"/></svg></i>No Scope of Practice Limits</div>
  <div class="check" style="left:241px;top:243px"><i><svg width="11" height="9" viewBox="0 0 11 9"><path d="M1 4.5l3 3L10 1" stroke="#fff" stroke-width="2" fill="none"/></svg></i>No Territory Fees</div>
  <div class="check" style="left:241px;top:294px"><i><svg width="11" height="9" viewBox="0 0 11 9"><path d="M1 4.5l3 3L10 1" stroke="#fff" stroke-width="2" fill="none"/></svg></i>No Convention Fees</div>
  <div class="check" style="left:697px;top:140px"><i><svg width="11" height="9" viewBox="0 0 11 9"><path d="M1 4.5l3 3L10 1" stroke="#fff" stroke-width="2" fill="none"/></svg></i>No Monthly Licensing Fees</div>
  <div class="check" style="left:697px;top:191px"><i><svg width="11" height="9" viewBox="0 0 11 9"><path d="M1 4.5l3 3L10 1" stroke="#fff" stroke-width="2" fill="none"/></svg></i>No % Royalties</div>
  <div class="check" style="left:697px;top:243px"><i><svg width="11" height="9" viewBox="0 0 11 9"><path d="M1 4.5l3 3L10 1" stroke="#fff" stroke-width="2" fill="none"/></svg></i>No % Advertising Fees</div>
  <div class="check" style="left:697px;top:294px"><i><svg width="11" height="9" viewBox="0 0 11 9"><path d="M1 4.5l3 3L10 1" stroke="#fff" stroke-width="2" fill="none"/></svg></i>No Mandatory Vendors</div>
</section>

<section class="abs steps">
  <div class="abs world" role="img" aria-label="Faint grey world map background"></div>
  <div class="abs kicker" style="left:0;width:1200px;text-align:center;top:50px;font-size:18px">It's Easy</div>
  <h2 class="section-title" style="position:absolute;left:0;width:1200px;top:78px;font-size:35px">GET STARTED TODAY</h2>

  <svg class="abs" style="left:0;top:180px" width="1200" height="200" viewBox="0 0 1200 200" fill="none">
    <g>
      <circle cx="275" cy="103" r="92" stroke="var(--red)" stroke-width="2.5"/>
      <circle cx="275" cy="103" r="72" stroke="#ddd" stroke-dasharray="3 4"/>
      <circle cx="337" cy="38" r="24" fill="#fff"/>
      <path d="M367 108h38M396 99l9 9-9 9" stroke="var(--red)" stroke-width="2.5"/>
      <path d="M254 88c-2 0-4 2-4 4 0 18 14 32 32 32 2 0 4-2 4-4v-6l-8-3-4 4c-5-3-9-7-12-12l4-4-3-8z" stroke="var(--blue)" stroke-width="2"/>
      <rect x="270" y="80" width="24" height="17" stroke="var(--blue)" stroke-width="2"/>
      <path d="M270 80l12 9 12-9" stroke="var(--blue)" stroke-width="2"/>
    </g>
    <g>
      <circle cx="586" cy="103" r="92" stroke="var(--red)" stroke-width="2.5"/>
      <circle cx="586" cy="103" r="72" stroke="#ddd" stroke-dasharray="3 4"/>
      <circle cx="660" cy="38" r="24" fill="#fff"/>
      <path d="M678 108h38M707 99l9 9-9 9" stroke="var(--red)" stroke-width="2.5"/>
      <path d="M586 132s-18-20-18-34a18 18 0 0136 0c0 14-18 34-18 34z" stroke="var(--blue)" stroke-width="2"/>
      <circle cx="586" cy="97" r="8" stroke="var(--blue)" stroke-width="2"/>
      <path d="M582 97l3 3 5-5" stroke="var(--blue)" stroke-width="1.6"/>
      <path d="M572 136h28" stroke="var(--blue)" stroke-width="2"/>
    </g>
    <g>
      <circle cx="908" cy="103" r="92" stroke="var(--red)" stroke-width="2.5"/>
      <circle cx="908" cy="103" r="72" stroke="#ddd" stroke-dasharray="3 4"/>
      <circle cx="986" cy="38" r="24" fill="#fff"/>
      <path d="M1000 108h38M1029 99l9 9-9 9" stroke="var(--red)" stroke-width="2.5"/>
      <rect x="880" y="78" width="56" height="40" stroke="var(--blue)" stroke-width="2"/>
      <path d="M876 78h64M908 118v10M898 128h20" stroke="var(--blue)" stroke-width="2"/>
      <rect x="894" y="88" width="28" height="20" stroke="var(--blue)" stroke-width="2"/>
      <path d="M904 92v12l9-6z" stroke="var(--blue)" stroke-width="1.8"/>
    </g>
    <text x="337" y="49" text-anchor="middle" font-family="Figtree,Arial,sans-serif" font-weight="700" font-size="28" fill="var(--red)">1</text>
    <text x="660" y="49" text-anchor="middle" font-family="Figtree,Arial,sans-serif" font-weight="700" font-size="28" fill="var(--red)">2</text>
    <text x="986" y="49" text-anchor="middle" font-family="Figtree,Arial,sans-serif" font-weight="700" font-size="28" fill="var(--red)">3</text>
  </svg>

  <div class="step" style="left:145px;top:389px"><h3>Contact Us</h3><p>Contact us for more information<br>on our model</p></div>
  <div class="step" style="left:456px;top:389px"><h3>Visit Us</h3><p>chedule a time to visit Atlanta<br>and see our clinics in action</p></div>
  <div class="step" style="left:778px;top:389px"><h3>Schedule a Webinar</h3><p>Schedule your one-on-one 20<br>minute webinar more+</p></div>
</section>

<section class="abs badges">
  <div class="badge" role="img" aria-label="Accreditation badge" style="left:317px;top:19px;width:95px;height:95px;border-radius:50%;background:#1f5d9c"></div>
  <div class="badge" role="img" aria-label="Medical society membership badge" style="left:466px;top:22px;width:240px;height:90px;border-radius:6px;background:#e3e0ea"></div>
  <div class="badge" role="img" aria-label="Professional academy membership badge" style="left:804px;top:24px;width:124px;height:84px;background:#2b3f73"></div>
</section>

<div class="abs contact-photo" role="img" aria-label="Photo of a smiling doctor measuring a young woman's waist with a tape measure"></div>
<section class="abs contact">
  <div class="abs" style="left:63px;top:59px;font-family:Figtree,Arial,sans-serif;font-weight:600;font-size:12px;color:var(--red)">Contact Us</div>
  <h2 class="abs" style="left:62px;top:84px;font-family:Figtree,Arial,sans-serif;font-weight:700;font-size:34px;color:#fff">Today to Learn More</h2>
  <div class="field" style="left:69px;top:166px;width:224px;height:41px">Name</div>
  <div class="field" style="left:308px;top:166px;width:223px;height:41px">Email</div>
  <div class="field" style="left:69px;top:227px;width:224px;height:39px">Phone</div>
  <div class="field" style="left:308px;top:227px;width:223px;height:39px">Country/State</div>
  <div class="field" style="left:69px;top:287px;width:462px;height:201px">Message</div>
  <div class="btn btn-red" style="left:69px;top:524px;width:153px;height:40px">Contact Now</div>
</section>

<footer class="abs footer">
  <div class="abs brand-name" style="left:85px;top:130px">Bluefern<br>Slimming Clinic</div>
  <div class="f-info" style="left:85px;top:209px">
    <svg width="12" height="15" viewBox="0 0 12 15" style="margin-top:4px"><path d="M6 14S1 8.5 1 5.5a5 5 0 0110 0C11 8.5 6 14 6 14z" stroke="#fff" fill="none" stroke-width="1.3"/><circle cx="6" cy="5.5" r="1.8" fill="#fff"/></svg>
    <span>4410 Linden Mill Road<br>Suite 210, Brookhaven, GA 30319</span>
  </div>
  <div class="f-info" style="left:85px;top:263px;color:var(--red)">
    <svg width="12" height="12" viewBox="0 0 24 24" style="margin-top:5px"><path d="M6.6 10.8a15 15 0 006.6 6.6l2.2-2.2c.3-.3.7-.4 1-.2 1.1.4 2.3.6 3.6.6.6 0 1 .4 1 1V20c0 .6-.4 1-1 1A17 17 0 013 4c0-.6.4-1 1-1h3.5c.6 0 1 .4 1 1 0 1.3.2 2.5.6 3.6.1.3 0 .7-.2 1z" fill="#fff"/></svg>
    <span>(877) 555-0142</span>
  </div>
  <div class="f-info" style="left:85px;top:296px;color:var(--red)">
    <svg width="13" height="10" viewBox="0 0 13 10" style="margin-top:6px"><rect x=".5" y=".5" width="12" height="9" stroke="#fff" fill="none"/><path d="M1 1l5.5 4.5L12 1" stroke="#fff" fill="none"/></svg>
    <span>hello@harrowvalecourses.com</span>
  </div>

  <div class="abs f-head" style="left:514px;top:158px">QUICK LINKS</div>
  <span class="f-link" style="left:520px;top:200px">HOME</span>
  <span class="f-link" style="left:520px;top:231px">ABOUT US</span>
  <span class="f-link" style="left:520px;top:262px">WHAT WE OFFER</span>
  <span class="f-link" style="left:520px;top:293px">COMPARE</span>
  <span class="f-link" style="left:520px;top:324px">FAQ</span>
  <span class="f-link" style="left:520px;top:355px">CONTACT</span>

  <div class="abs f-head" style="left:782px;top:158px">NEWSLETTER</div>
  <div class="abs" style="left:783px;top:194px;font-size:13px">Lorem ipsum dolor sit amet,</div>
  <div class="abs" style="left:784px;top:234px;width:353px;height:42px;border:1px solid #4a5872;border-radius:3px;display:flex;overflow:hidden">
    <div style="flex:1;padding:13px 20px;font-family:Figtree,Arial,sans-serif;font-size:11.5px;color:#fff">Your Mail</div>
    <div style="width:95px;background:var(--red);display:flex;align-items:center;justify-content:center;font-family:Figtree,Arial,sans-serif;font-weight:700;font-size:12px">Subscribe</div>
  </div>

  <div class="abs f-rule"></div>
  <div class="abs" style="left:0;width:1200px;top:459px;text-align:center;font-size:11.5px">© 2023 Bluefern Slimming, Inc. All rights reserved</div>
</footer>

</body>
</html>
```